DAWL Tea & Herbal Tea Packaging Labels

We are seeking new consistent front label designs that we can use for both retail and wholesale packaging purposes:

DAWL PHILOSOPHY

DAWL provides a selection of ‘energy enhanced’ signature infusion blends that taste great while assisting a person deeply on several levels – emotional, mental, physical and spiritual.

We source quality ingredients and specifically use certified organic, spray free and wildcrafted ingredients for our herbal blends.

DAWL’s PRODUCT RANGE

A. 6 standard signature herbal blends (standard range)
B. 2 seasonal blends - which change every quarter (1 x herbal blend, 1 x tea-based blend)
C. selection of teas – black, green, white, oolong (which vary in type and number)
D. custom and limited edition blends – herbal and teas
E. tea drinking accessories.

11 LABELS ARE REQUIRED

Labels 1-8 for Herbal Blends (to be denoted by an accent of SILVER)
Labels 9-10 for Teas (to be denoted by an accent of GOLD)
Label 11 for Accessories

LABEL SIZE

Current front label dimensions: 63.5 x 72mm long – willing to look at alternate label size
Current ‘usable area’ of smallest resealable bag: 110 x 130mm long

** PLEASE SEE ATTACHED WORD DOC FOR COMPLETE SPECIFICATION - PLEASE READ BEFORE COMMENCING ANY WORK **
Updates

hi,

forgot to include an attachment of the current labels for herbal teas that are used... here is a link to the PDF.

http://files.quorvane.example/u/47381652/DAWL-Herbal-Labels.pdf

thanks Malcolm

Hi,

please note we have attached a jpg of the packaging the label goes onto... it is in the attached files in the brief - called packaging.

thanks Malcolm

Hi, we've uploaded some pics of the current packaging to give you a sense of the packaging we are using and the space on the front pack to work with.

many thanks.

Target Market(s)

Women and men aged 30-55 with an interest in natural products, emotional/spiritual wellbeing and support.

DAWL DISTRIBUTION

Online store for retail sales,
Cafes for food service,
Practitioner (naturopaths, massage therapists, energy healers) clinics and stores.

Industry/Entity Type

Retail

Requirements
Must have
• Each label should have:
• Current logo and tagline;
• Website name;
• Silver accent for herbal range labels;
• Gold accent for tea range labels;
• Colour-coding for the 6 signature herbals.
• ** PLEASE SEE ATTACHED WORD DOC FOR COMPLETE SPECIFICATION - PLEASE READ BEFORE COMMENCING ANY WORK **
Nice to have
• Mrs Eaves font for text (to match logo font type)

```html
<!DOCTYPE html>
<html lang="en">
<head>
<meta charset="utf-8">
<title>DAWL Herbal Tea Label</title>
<link rel="stylesheet" href="https://fonts.googleapis.com/css2?family=EB+Garamond:ital,wght@0,400;1,400&family=Great+Vibes&family=PT+Sans:ital@0;1&display=swap">
<style>
  :root {
    --gold: #c99a16;
    --navy: #0e3a50;
    --paper: #f4f6f5;
    --leaf: #dde3e2;
    --white: #ffffff;
    --ink: #1b1b1b;
    --pink: #e2178a;
  }
  html, body {
    margin: 0;
    width: 1200px;
    height: 900px;
    overflow: hidden;
    background: var(--white);
  }
  .label {
    position: relative;
    width: 1200px;
    height: 900px;
  }
  .gold-frame {
    position: absolute;
    left: 95px; top: 17px;
    width: 998px; height: 843px;
    background: var(--gold);
  }
  .leaf-ground {
    position: absolute;
    left: 120px; top: 40px;
    width: 948px; height: 798px;
    background: radial-gradient(circle at 30% 40%, var(--leaf), var(--paper) 70%);
  }
  .title-band {
    position: absolute;
    left: 698px; top: 17px;
    width: 174px; height: 843px;
    background: var(--navy);
  }
  .vertical {
    position: absolute;
    writing-mode: vertical-rl;
    text-align: center;
    margin: 0;
    white-space: nowrap;
  }
  .range-title {
    left: 722px; top: 40px;
    height: 800px;
    font-family: "Great Vibes", cursive;
    font-weight: 400;
    font-size: 112px;
    line-height: 126px;
    color: var(--white);
  }
  .brand-name {
    left: 925px; top: 170px;
    height: 280px;
    font-family: "PT Sans", sans-serif;
    font-size: 72px;
    line-height: 80px;
    letter-spacing: 6px;
    color: var(--ink);
  }
  .blend-panel {
    position: absolute;
    left: 342px; top: 86px;
    width: 318px; height: 709px;
    background: var(--navy);
  }
  .blend-card {
    position: absolute;
    left: 20px; top: 20px;
    width: 280px; height: 669px;
    background: var(--white);
  }
  .blend-name {
    left: 196px; top: 0;
    height: 669px;
    font-family: "Great Vibes", cursive;
    font-weight: 400;
    font-size: 50px;
    line-height: 64px;
    color: var(--ink);
  }
  .blend-brief {
    left: 153px; top: 0;
    height: 669px;
    font-family: "Great Vibes", cursive;
    font-size: 28px;
    line-height: 40px;
    color: var(--ink);
  }
  .blend-ingredients {
    left: 68px; top: 0;
    height: 669px;
    font-family: "EB Garamond", serif;
    font-size: 17.5px;
    line-height: 25px;
    color: var(--ink);
  }
  .blend-growing {
    left: 16px; top: 0;
    height: 669px;
    font-family: "EB Garamond", serif;
    font-style: italic;
    font-size: 21px;
    line-height: 30px;
    color: var(--ink);
  }
  .serving {
    left: 252px; top: 40px;
    height: 798px;
    font-family: "PT Sans", sans-serif;
    font-style: italic;
    font-size: 18px;
    line-height: 27px;
    color: var(--ink);
  }
  .website, .slogan {
    font-family: "PT Sans", sans-serif;
    font-style: italic;
    font-size: 27px;
    line-height: 34px;
    color: var(--pink);
    text-align: start;
  }
  .website { left: 168px; top: 98px; }
  .slogan { left: 168px; top: 470px; }
  .cup-art {
    position: absolute;
    left: 165px; top: 690px;
    width: 100px; height: 100px;
    border-radius: 40%;
    background: radial-gradient(circle, #fbd3e8, #f6a9cf);
  }
</style>
</head>
<body>
  <div class="label">
    <div class="gold-frame"></div>
    <div class="leaf-ground" role="img" aria-label="Soft grey leaf and vine pattern background"></div>
    <div class="title-band"></div>

    <h1 class="vertical range-title">Herbal Tea</h1>

    <p class="vertical brand-name">DAWL</p>

    <div class="blend-panel">
      <div class="blend-card">
        <h2 class="vertical blend-name">Name of Blend</h2>
        <p class="vertical blend-brief">Brief description of blend</p>
        <p class="vertical blend-ingredients">This is the text for the specific ingredients within the blend.<br>This is the text for the specific ingredients within the blend.<br>This is the text for the specific ingredients within the blend.</p>
        <p class="vertical blend-growing">Growing conditions of ingredients</p>
      </div>
    </div>

    <p class="vertical serving">Serving: for optimum flavour pour freshly boiled water over<br>one generous teaspoon per cup and steep 3 – 5 mins</p>

    <p class="vertical website">www.dawl.com.au</p>
    <p class="vertical slogan">love in every cup</p>
    <div class="cup-art" role="img" aria-label="Pink line illustration of a teacup with small flowers"></div>
  </div>
</body>
</html>
```